Hallvard
Veneer Technology
Hallvard - Agriculture
Creative Brief
Agriculture
http://hallvard-veneertechnology.example
We have 4 different product lines.
1. Stone-Veneer
2.Sonic-Paneltrim
3.Plexard
4.Moravelt
We do not installl any products. We just distribute them to architects, companies, builders, ect.
The stone can be made for any products. From laptops, countertops, "wall paper", notebooks, smart car, sinks, ect.
Dislikes: -it's hard to see what our company is -appearance -professionalism -pictures -it's not appealing
Nature
Gray, white and blacks
Blues
Red (Nothing too bright!)
below header
http://www.brevicott.example
http://www.folmaneq.example/
http://4plank.example

```html
<!DOCTYPE html>
<html lang="en">
<head>
<meta charset="utf-8">
<title>Hallvard Veneer Technology</title>
<link href="https://fonts.googleapis.com/css2?family=Arimo:wght@400;700&display=swap" rel="stylesheet">
<style>
:root{
  --red:#c0121b;
  --red-dark:#8f0d13;
  --ink:#222;
  --muted:#666;
  --line:#d8d8d8;
  --bg:#ffffff;
  --footer:#e6e6e6;
}
*{box-sizing:border-box;margin:0;padding:0}
html,body{width:1200px;height:1059px;overflow:hidden;background:var(--bg);font-family:"Arimo",Arial,sans-serif;color:var(--ink)}
.page{position:relative;width:1200px;height:1059px}
.brand{position:absolute;left:109px;top:50px;font-size:30px;font-weight:700;color:var(--ink);line-height:1}
.contact{position:absolute;right:100px;top:46px;text-align:right}
.contact small{display:block;font-size:15px;color:#333}
.contact strong{display:block;font-size:36px;font-weight:400;color:#111;line-height:1.1}
.nav{position:absolute;left:109px;top:114px;width:991px;height:36px;background:linear-gradient(var(--red),var(--red-dark));display:flex;align-items:center;padding-left:30px;gap:62px}
.nav a{color:#fff;text-decoration:none;font-size:18px}
.hero{position:absolute;left:109px;top:157px;width:991px;height:271px;background:linear-gradient(160deg,#b06a35,#7a3a17 55%,#5a2a10);border:1px solid #ccc}
.hero-caption{position:absolute;left:0;right:0;bottom:8px;height:44px;background:rgba(0,0,0,.45);color:#fff;font-size:17px;line-height:44px;text-align:center}
.section-title{position:absolute;left:109px;top:444px;font-size:24px;font-weight:400;color:#111;display:flex;align-items:center;gap:12px}
.section-title::before{content:"";width:13px;height:13px;border-radius:50%;background:#bbb}
.product{position:absolute;width:263px;height:138px;border:1px solid #ccc}
.product span{position:absolute;left:0;right:0;bottom:10px;height:34px;background:rgba(0,0,0,.55);color:#fff;font-size:22px;line-height:34px;text-align:center}
.p1{left:109px;top:491px;background:linear-gradient(135deg,#8d7a6a,#5e4c40)}
.p2{left:423px;top:491px;background:linear-gradient(135deg,#f1ede6,#c9beb2)}
.p3{left:109px;top:666px;background:linear-gradient(135deg,#cfd2d6,#9a9ea3)}
.p4{left:423px;top:666px;background:linear-gradient(135deg,#b4693a,#7d3e1c)}
.about-title{position:absolute;left:109px;top:836px;font-size:26px;font-weight:400}
.about-text{position:absolute;left:109px;top:872px;width:580px;font-size:15px;line-height:18px;color:#333}
.quote{position:absolute;left:751px;top:450px;width:364px;height:480px;border:1px solid var(--line);border-radius:6px;box-shadow:0 0 6px rgba(0,0,0,.1)}
.quote-head{position:absolute;left:-6px;top:10px;width:266px;height:52px;background:linear-gradient(var(--red),var(--red-dark));color:#fff;font-size:22px;line-height:52px;padding-left:30px;border-radius:0 26px 26px 0}
.quote-intro{position:absolute;left:26px;top:76px;width:320px;font-size:14px;line-height:17px;color:#777}
.field{position:absolute;left:26px;font-size:14px;color:#333}
.field i{position:absolute;left:104px;top:-8px;width:204px;height:32px;border:1px solid #ccc;border-radius:3px}
.f1{top:170px}.f2{top:210px}.f3{top:250px}.f4{top:292px}
.select-arrow{position:absolute;right:0;top:0;width:30px;height:30px;border-left:1px solid #ccc;background:#f2f2f2}
.message{position:absolute;left:26px;top:334px;width:308px;height:76px;border:1px solid #ccc;border-radius:3px}
.submit{position:absolute;left:256px;top:429px;width:84px;height:38px;background:linear-gradient(var(--red),var(--red-dark));color:#fff;font-weight:700;font-size:16px;line-height:38px;text-align:center;border-radius:3px}
.footer{position:absolute;left:0;top:989px;width:1200px;height:70px;background:var(--footer)}
.footer-links{position:absolute;left:109px;top:18px;font-size:13px;color:#333}
.footer-copy{position:absolute;left:109px;top:36px;font-size:13px;color:#888}
.footer-brand{position:absolute;right:100px;top:22px;font-size:15px;font-weight:700;color:#444}
</style>
</head>
<body>
<div class="page">
  <div class="brand">Hallvard Veneer Technology</div>
  <div class="contact"><small>Call for Consultation</small><strong>888-555-0147</strong></div>

  <nav class="nav"><a>Home</a><a>News</a><a>Products</a><a>Corporate Social Responsibility</a><a>Contact Us</a></nav>

  <div class="hero" role="img" aria-label="Woodworking tools on a wooden veneer surface">
    <div class="hero-caption">Your Partner for Innovative Architectural Elements, Architectural Woodworking, Design Features and Furniture Manufacturing.</div>
  </div>

  <h2 class="section-title">Our Products</h2>
  <div class="product p1" role="img" aria-label="Stone veneer sheet"><span>Stone-Veneer</span></div>
  <div class="product p2" role="img" aria-label="Acoustic panel"><span>Sonic-Paneltrim</span></div>
  <div class="product p3" role="img" aria-label="Wall panel system"><span>Plexard</span></div>
  <div class="product p4" role="img" aria-label="Wooden acoustic slats"><span>Moravelt</span></div>

  <h2 class="about-title">About Us</h2>
  <p class="about-text">Este natus error sit voluptatem accusantium doloremque laudantium, totam rem aperiam, site natus error sit voluptatem accusantium doloremque laudantium, totam rem Natus error sit voluptatem accusantium doloremque laudantium, totam rem aperiam.</p>

  <form class="quote">
    <div class="quote-head">Request for a Quote</div>
    <p class="quote-intro">For further information on how we can help you, please fill in the form below and we will get in contact with you shortly.</p>
    <label class="field f1">First Name<i></i></label>
    <label class="field f2">Last Name<i></i></label>
    <label class="field f3">Email<i></i></label>
    <label class="field f4">State<i><span class="select-arrow"></span></i></label>
    <div class="message"></div>
    <div class="submit">SUBMIT</div>
  </form>

  <footer class="footer">
    <div class="footer-links">Terms of Use | Privacy Policy</div>
    <div class="footer-copy">Copyright 2011. All Right Reserved by Hallvard</div>
    <div class="footer-brand">Hallvard</div>
  </footer>
</div>
</body>
</html>
```